VELMA GIFTS - Gift Card app

We have created an application to sell gift cards and greeting cards for Brisket Shop and Tandor Mart. Layout to remain the same, upgrade and change the graphics. Keep the background white. Must fit into existing app.

Logo design + 4 tutorial slides + 1 main page. The 5 current images are included and red box around what we want changed.

Pay particular attention to the red squares.

```html
<!DOCTYPE html>
<html lang="en">
<head>
<meta charset="utf-8">
<title>VELMA GIFTS – App Screens</title>
<link rel="stylesheet" href="https://fonts.googleapis.com/css2?family=Nunito:wght@400;600;700;800;900&display=swap">
<style>
  :root {
    --brand-red: #c4101c;
    --ink: #1f2326;
    --ink-soft: #555b60;
    --muted: #8b9095;
    --rule: #cfd3d6;
    --dot: #c9cccf;
    --pill-blue: #1a7bf0;
    --canvas: #ffffff;
    --screen-bg: #ffffff;
    --chip-bg: #eef0f2;
  }
  * { box-sizing: border-box; margin: 0; padding: 0; }
  html, body { width: 1200px; height: 970px; overflow: hidden; background: var(--canvas); }
  body { position: relative; font-family: "Nunito", sans-serif; color: var(--ink); }

  .screen { position: absolute; background: var(--screen-bg); overflow: hidden; }
  .screen--splash {
    left: 76px; top: 78px; width: 184px; height: 401px;
    background: var(--brand-red); border-radius: 22px;
  }
  .screen--tutorial, .screen--recipient {
    top: 68px; width: 368px; height: 838px;
    box-shadow: 0 0 6px rgba(0,0,0,0.08);
  }
  .screen--tutorial { left: 333px; }
  .screen--recipient { left: 772px; }

  /* splash */
  .splash-brand {
    position: absolute; left: 0; right: 0; top: 100px;
    display: flex; align-items: center; justify-content: center; gap: 6px;
    color: #fff; font-weight: 800; font-size: 13px; letter-spacing: 1px;
  }
  .splash-brand .mark { width: 12px; height: 12px; background: #fff; }
  .splash-art {
    position: absolute; left: 6px; top: 172px; width: 172px; height: 112px;
    background: radial-gradient(ellipse at 50% 50%, #f3b8bd 0%, #e0404c 60%, rgba(196,16,28,0) 100%);
  }
  .splash-footer {
    position: absolute; left: 0; right: 0; bottom: 0; height: 15px;
    background: #fff; font-size: 5px; color: var(--muted);
    display: flex; align-items: center; justify-content: center;
  }

  /* status bar */
  .status-time {
    position: absolute; left: 27px; top: 9px; width: 61px; height: 21px;
    background: var(--pill-blue); color: #fff; border-radius: 11px;
    font-size: 14px; font-weight: 600; display: flex; align-items: center; justify-content: center;
  }
  .status-icons { position: absolute; right: 22px; top: 14px; }

  /* brand lockup */
  .brand {
    position: absolute; left: 0; right: 0;
    display: flex; align-items: center; justify-content: center; gap: 7px;
    color: var(--brand-red); font-weight: 800; letter-spacing: 1px;
  }
  .brand .mark { background: var(--brand-red); }

  /* tutorial */
  .screen--tutorial .brand { top: 78px; font-size: 17px; }
  .screen--tutorial .brand .mark { width: 16px; height: 16px; }
  .eyebrow { position: absolute; top: 157px; width: 100%; text-align: center; font-size: 13.5px; font-weight: 600; color: var(--ink-soft); letter-spacing: .5px; }
  .slide-title { position: absolute; top: 180px; width: 100%; text-align: center; font-size: 27px; font-weight: 900; }
  .slide-art {
    position: absolute; left: 28px; top: 234px; width: 311px; height: 294px;
    background: radial-gradient(ellipse at 55% 50%, #f7a6ad 0%, #fbd9dc 50%, rgba(255,255,255,0) 72%);
  }
  .slide-caption { position: absolute; top: 560px; left: 12px; right: 12px; text-align: center; font-size: 15px; line-height: 18px; color: var(--ink-soft); }
  .pager { position: absolute; top: 645px; left: 0; right: 0; display: flex; justify-content: center; gap: 7px; align-items: center; }
  .pager span { width: 7px; height: 7px; border-radius: 50%; background: var(--dot); }
  .pager .is-active { width: 18px; border-radius: 4px; background: var(--ink); }

  .btn-primary {
    position: absolute; height: 46px; border-radius: 23px; background: var(--ink);
    color: #fff; font-size: 15px; font-weight: 600; display: flex; align-items: center; justify-content: center;
  }
  .screen--tutorial .btn-primary { left: 21px; width: 325px; top: 698px; }
  .screen--recipient .btn-primary { left: 19px; width: 330px; top: 692px; font-size: 16px; letter-spacing: .5px; }

  .opt-out { position: absolute; top: 765px; left: 0; right: 0; display: flex; justify-content: center; align-items: center; gap: 9px; font-size: 13.5px; color: var(--ink-soft); font-weight: 600; }
  .opt-out .box { width: 23px; height: 23px; border: 1.5px solid var(--ink-soft); border-radius: 4px; }
  .home-bar { position: absolute; bottom: 9px; left: 50%; margin-left: -69px; width: 138px; height: 4px; border-radius: 2px; background: var(--ink); }

  /* recipient */
  .icon-chip { position: absolute; top: 66px; width: 38px; height: 38px; border-radius: 50%; background: var(--chip-bg); display: flex; align-items: center; justify-content: center; }
  .icon-chip--menu { left: 22px; }
  .icon-chip--cart { left: 307px; }
  .cart-badge { position: absolute; top: -5px; right: -4px; width: 15px; height: 15px; border-radius: 50%; background: var(--brand-red); color: #fff; font-size: 10px; font-weight: 700; display: flex; align-items: center; justify-content: center; }
  .screen--recipient .brand { top: 75px; font-size: 13px; }
  .screen--recipient .brand .mark { width: 12px; height: 12px; }

  .stepper { position: absolute; top: 126px; left: 0; right: 0; height: 52px; border-bottom: 1px solid #e3e5e7; }
  .stepper-line { position: absolute; top: 9px; left: 50px; right: 40px; height: 1px; background: #e3e5e7; }
  .step { position: absolute; top: 0; text-align: center; font-size: 13.5px; font-weight: 700; }
  .step .num { display: block; margin: 0 auto 4px; width: 19px; height: 19px; border-radius: 50%; background: #fff; font-size: 12px; line-height: 19px; position: relative; }
  .step.is-current .num { background: var(--brand-red); color: #fff; }
  .step--1 { left: 19px; } .step--2 { left: 135px; } .step--3 { left: 281px; }

  .hero-art {
    position: absolute; left: 168px; top: 192px; width: 200px; height: 212px; z-index: 1;
    background: radial-gradient(ellipse at 60% 45%, #f59aa3 0%, #f9c4c9 40%, #fde6e8 62%, rgba(255,255,255,0) 78%);
  }
  .hero-title { position: absolute; left: 20px; top: 296px; z-index: 2; font-size: 30px; font-weight: 900; line-height: 37px; }
  .intro { position: absolute; left: 20px; top: 424px; width: 290px; font-size: 15px; line-height: 18px; color: var(--ink-soft); }
  .field { position: absolute; left: 20px; width: 330px; border-bottom: 1.5px solid var(--rule); }
  .field-label { display: block; font-size: 11px; color: var(--muted); margin-bottom: 8px; }
  .field-label em { font-style: italic; }
  .field-value { display: block; font-size: 15.5px; padding-bottom: 8px; }
  .field--name { top: 472px; } .field--email { top: 536px; } .field--country { top: 601px; }
  .field--country .field-label { font-size: 13px; margin-bottom: 12px; }
  .field--country .caret { position: absolute; right: 8px; bottom: 14px; }
</style>
</head>
<body>

  <section class="screen screen--splash" aria-label="Splash screen">
    <div class="splash-brand"><span class="mark"></span>VELMA GIFTS</div>
    <div class="splash-art" role="img" aria-label="Illustration of a small shop and shopping phone in red tones"></div>
    <div class="splash-footer">© 2023 Velma Gifts. All rights reserved.</div>
  </section>

  <section class="screen screen--tutorial" aria-label="Tutorial slide: Checkout">
    <div class="status-time">9:27</div>
    <svg class="status-icons" width="68" height="14" viewBox="0 0 68 14">
      <rect x="0" y="9" width="3" height="4" fill="#1f2326"/><rect x="5" y="6" width="3" height="7" fill="#1f2326"/>
      <rect x="10" y="3" width="3" height="10" fill="#c9cccf"/><rect x="15" y="0" width="3" height="13" fill="#c9cccf"/>
      <path d="M24 5 a11 11 0 0 1 15 0 M27 8 a6 6 0 0 1 9 0" stroke="#1f2326" stroke-width="2" fill="none"/><circle cx="31.5" cy="11" r="1.8" fill="#1f2326"/>
      <rect x="44" y="1" width="21" height="11" rx="3" fill="none" stroke="#1f2326" stroke-width="1.2"/><rect x="46" y="3" width="17" height="7" rx="1.5" fill="#1f2326"/><rect x="66" y="5" width="1.5" height="3" fill="#1f2326"/>
    </svg>
    <div class="brand"><span class="mark"></span>VELMA GIFTS</div>
    <p class="eyebrow">How it works</p>
    <h1 class="slide-title">Checkout</h1>
    <div class="slide-art" role="img" aria-label="Isometric illustration of online checkout: laptop storefront, shopping bags, card terminal and delivery scooter"></div>
    <p class="slide-caption">Complete your order and select a delivery method<br>for your digital gift</p>
    <div class="pager"><span></span><span></span><span></span><span class="is-active"></span></div>
    <div class="btn-primary">Get Started!</div>
    <div class="opt-out"><span class="box"></span>Don't show it again</div>
    <div class="home-bar"></div>
  </section>

  <section class="screen screen--recipient" aria-label="Recipient details">
    <div class="status-time">9:28</div>
    <svg class="status-icons" width="68" height="14" viewBox="0 0 68 14">
      <rect x="0" y="9" width="3" height="4" fill="#1f2326"/><rect x="5" y="6" width="3" height="7" fill="#1f2326"/>
      <rect x="10" y="3" width="3" height="10" fill="#c9cccf"/><rect x="15" y="0" width="3" height="13" fill="#c9cccf"/>
      <path d="M24 5 a11 11 0 0 1 15 0 M27 8 a6 6 0 0 1 9 0" stroke="#1f2326" stroke-width="2" fill="none"/><circle cx="31.5" cy="11" r="1.8" fill="#1f2326"/>
      <rect x="44" y="1" width="21" height="11" rx="3" fill="none" stroke="#1f2326" stroke-width="1.2"/><rect x="46" y="3" width="17" height="7" rx="1.5" fill="#1f2326"/><rect x="66" y="5" width="1.5" height="3" fill="#1f2326"/>
    </svg>
    <div class="icon-chip icon-chip--menu">
      <svg width="20" height="14" viewBox="0 0 20 14"><path d="M0 1h20M0 7h20M0 13h20" stroke="#1f2326" stroke-width="1.8"/></svg>
    </div>
    <div class="brand"><span class="mark"></span>VELMA GIFTS</div>
    <div class="icon-chip icon-chip--cart">
      <svg width="20" height="18" viewBox="0 0 20 18"><path d="M1 1h3l2.5 10h10l2-7H5.5" stroke="#1f2326" stroke-width="1.6" fill="none" stroke-linejoin="round"/><circle cx="8" cy="15" r="1.5" fill="#1f2326"/><circle cx="15" cy="15" r="1.5" fill="#1f2326"/></svg>
      <span class="cart-badge">2</span>
    </div>

    <nav class="stepper">
      <div class="stepper-line"></div>
      <div class="step step--1 is-current"><span class="num">1</span>Recipient</div>
      <div class="step step--2"><span class="num">2</span>Greeting Card</div>
      <div class="step step--3"><span class="num">3</span>Gift Cards</div>
    </nav>

    <div class="hero-art" role="img" aria-label="Isometric illustration of people celebrating with hearts and stars"></div>
    <h1 class="hero-title">Feeling<br>grateful for<br>someone?</h1>
    <p class="intro">Enter your recipient information to send<br>your perfect digital gift</p>

    <div class="field field--name"><span class="field-label">Name of Recipient</span><span class="field-value">Tomas</span></div>
    <div class="field field--email"><span class="field-label">Email of Recipient <em>(optional)</em></span><span class="field-value">tomas@lorvex.com</span></div>
    <div class="field field--country"><span class="field-label">Country</span><span class="field-value">Canada</span>
      <svg class="caret" width="18" height="11" viewBox="0 0 18 11"><path d="M0 0h18L9 11z" fill="#1f2326"/></svg>
    </div>

    <div class="btn-primary">Continue</div>
    <div class="home-bar"></div>
  </section>

</body>
</html>
```